Business card design needed

I am a small start up business in the mortgage broking industry based in Sydney called 'keys2nest'. I will be providing residential mortgages to first home owners, investors and people looking to refinance. I would like to see designs that use the colors blue, black, and white - same as my logo (see logo design uploaded)

Target Market(s)

My target market is First Home Owners, property investors, and people looking to refinance. The loans I will be providing are for residential property only at this stage, and my clients will predominantly be in the 30-50yr age bracket.

Industry/Entity Type

Residential

Contact Information for Business Card

Owen Partridge
Director/Mobile Mortgage Broker
keys2nest
PO BOX 4287
Westmead NSW 2145
Mb: 0491 862 307
email: owen@keys2nest.com.au

Requirements
Must have
• please use lower case for business name (i.e. keys2nest)

```html
<!DOCTYPE html>
<html lang="en">
<head>
<meta charset="utf-8">
<title>keys2nest business card</title>
<link rel="stylesheet" href="https://fonts.googleapis.com/css2?family=Lato:ital,wght@0,400;0,700;1,400&display=swap">
<style>
  :root {
    --brand-blue: #009fda;
    --ink: #231f20;
    --paper: #ffffff;
    --page: #ffffff;
    --card-shadow: rgba(0, 0, 0, 0.14);
  }
  * { box-sizing: border-box; margin: 0; padding: 0; }
  html, body {
    width: 1184px;
    height: 1200px;
    overflow: hidden;
    background: var(--page);
    font-family: "Lato", Arial, sans-serif;
  }
  .canvas {
    position: relative;
    width: 1184px;
    height: 1200px;
  }
  .card {
    position: absolute;
    left: 100px;
    width: 980px;
    height: 530px;
    background: var(--paper);
    box-shadow: 0 2px 10px var(--card-shadow);
    overflow: hidden;
  }
  .card--front { top: 30px; }
  .card--back { top: 630px; }

  .card__band {
    position: absolute;
    left: 0;
    width: 100%;
    background: var(--brand-blue);
  }
  .card--front .card__band { top: 0; height: 150px; }
  .card--back .card__band { top: 150px; bottom: 0; }

  .holder {
    position: absolute;
    left: 18px;
    top: 20px;
    color: var(--paper);
  }
  .holder__name {
    font-weight: 700;
    font-size: 36px;
    line-height: 1.2;
  }
  .holder__role {
    font-style: italic;
    font-weight: 400;
    font-size: 28px;
    line-height: 1.3;
  }
  .contact {
    position: absolute;
    left: 18px;
    top: 166px;
    font-style: normal;
    font-size: 29px;
    line-height: 41px;
    color: var(--ink);
  }
  .wordmark {
    position: absolute;
    display: flex;
    align-items: center;
    gap: 14px;
    font-weight: 400;
    font-size: 48px;
    color: var(--ink);
    line-height: 1;
  }
  .wordmark__square {
    width: 30px;
    height: 30px;
    background: var(--brand-blue);
  }
  .card--front .wordmark { right: 34px; bottom: 42px; }
  .card--back .wordmark { left: 30px; top: 52px; }
</style>
</head>
<body>
<main class="canvas">
  <section class="card card--front" aria-label="Card front">
    <div class="card__band" aria-hidden="true"></div>
    <div class="holder">
      <p class="holder__name">Owen Partridge</p>
      <p class="holder__role">Director/Mobile Mortgage Broker</p>
    </div>
    <address class="contact">
      keys2nest PO BOX 4287<br>
      Westmead NSW 2145<br>
      Mb: 0491 862 307<br>
      email: owen@keys2nest.com.au
    </address>
    <div class="wordmark">
      <span class="wordmark__square" aria-hidden="true"></span>
      <span class="wordmark__name">keys2nest</span>
    </div>
  </section>

  <section class="card card--back" aria-label="Card back">
    <div class="card__band" aria-hidden="true"></div>
    <div class="wordmark">
      <span class="wordmark__square" aria-hidden="true"></span>
      <span class="wordmark__name">keys2nest</span>
    </div>
  </section>
</main>
</body>
</html>
```